prestige web design for KESTRAL Finance

Hi Guys,

Looking to team up with a creative designer for another of our websites for KESTRAL finance.
if looking for our similar website www.brimwellfinance.com.au is one of our other companies. ideally working in our logo being black and white.

Please see attachments for our logo and a description
HOME
VEHICLE
EQUIPMENT
WHO WE ARE
CONTACT US

open to ideas on layout .

touch base if you have any questions.

Target Market(s)

Prestige cars and equipment -trucks earthmoving

Industry/Entity Type

finance

Coding

Coded - Design and coding required

Number of Pages Required

5+ page

Font styles to use
Sans Serif

Colors

Designer to choose colors to be used in the design.

```html
<!DOCTYPE html>
<html lang="en">
<head>
<meta charset="utf-8">
<title>KESTRAL Finance</title>
<link href="https://fonts.googleapis.com/css2?family=Domine:wght@400;500;700&family=Nunito+Sans:wght@400;600;700;800&display=swap" rel="stylesheet">
<style>
:root{
  --ink:#111111;
  --black:#000000;
  --white:#ffffff;
  --muted:#3c3c3c;
  --soft:#f1f2f4;
  --line:#2a2a2a;
  --wave:#dfe5ec;
  --footer:#0b0b0b;
  --slate:#4b5560;
  --serif:'Domine', Georgia, serif;
  --sans:'Nunito Sans', Arial, sans-serif;
}
*{margin:0;padding:0;box-sizing:border-box}
html,body{width:1200px;height:4653px;overflow:hidden}
body{position:relative;background:var(--white);font-family:var(--sans);color:var(--ink)}
.abs{position:absolute}
.serif{font-family:var(--serif);font-weight:400}
p{font-size:13.5px;line-height:20.5px;color:var(--muted)}
.cta{display:flex;align-items:center;gap:14px;font-size:13px;font-weight:700}
.cta svg{width:28px;height:28px}
.hero{left:0;top:0;width:1200px;height:680px;background:linear-gradient(120deg,#5b5856 0%,#3e3c3b 45%,#2d2c2b 100%)}
.nav-logo{left:96px;top:44px;color:var(--white);font-weight:800;font-size:34px;letter-spacing:1px}
.nav{top:55px;color:var(--white);font-size:13px}
.hero-strip{border:2px solid rgba(255,255,255,.85)}
.dots{left:96px;top:528px;display:flex;gap:5px}
.dots span{width:9px;height:9px;border-radius:50%;background:var(--white)}
.dots span.off{background:transparent;border:1.5px solid var(--white)}
.wave-bg{background:linear-gradient(160deg,rgba(223,229,236,0) 20%,rgba(223,229,236,.9) 55%,rgba(223,229,236,0) 85%)}
.photo-city{background:linear-gradient(180deg,#c9d3dd 0%,#8a9cae 50%,#5b6570 100%)}
.photo-car{background:var(--slate)}
.vehicle-panel{left:517px;top:2040px;width:683px;height:479px;background:var(--black);color:var(--white)}
.vehicle-panel p{color:#e8e8e8}
.calc{left:679px;top:2600px;width:443px;height:450px;background:var(--white);box-shadow:0 4px 24px rgba(0,0,0,.12)}
.calc label{position:absolute;left:30px;font-size:13px}
.calc .field{position:absolute;left:205px;width:207px;height:30px;border:1.5px solid var(--line);font-size:13px;padding:6px 10px}
.calc .btn{position:absolute;left:299px;top:382px;width:122px;height:30px;border:1.5px solid var(--line);font-size:13px;text-align:center;line-height:27px}
.who-bg{left:0;top:3101px;width:1200px;height:1245px;background:var(--soft)}
.form-card{left:108px;top:3710px;width:497px;height:558px;background:var(--white);box-shadow:0 2px 14px rgba(0,0,0,.08)}
.form-card .input{position:absolute;left:24px;width:428px;height:40px;border:1.5px solid var(--line);font-size:15px;padding:10px 18px}
.contact-line{display:flex;align-items:flex-start;gap:14px;font-size:20px;color:var(--ink)}
.contact-line svg{width:24px;height:24px;flex:none;margin-top:2px}
.footer{left:0;top:4346px;width:1200px;height:307px;background:var(--footer);color:var(--white)}
.footer h4{font-family:var(--serif);font-weight:400;font-size:20px;position:absolute}
.footer .small{font-size:11.5px;line-height:16px;color:#f0f0f0}
.divider{position:absolute;width:1.5px;background:#555;top:36px;height:208px}
.flist{position:absolute;list-style:none;font-size:12.5px;line-height:25px}
.fcontact{position:absolute;display:flex;gap:12px;font-size:12.5px;line-height:17px}
.fcontact svg{width:15px;height:15px;flex:none}
</style>
</head>
<body>

<section class="hero abs" aria-label="Hero">
  <div class="abs" role="img" aria-label="Family relaxing together in a living room" style="inset:0;background:linear-gradient(100deg,rgba(90,86,82,.95),rgba(60,58,56,.9) 60%,rgba(40,40,40,.95))"></div>
  <div class="nav-logo abs">KESTRAL Finance</div>
  <span class="nav abs" style="left:512px">home</span>
  <span class="nav abs" style="left:605px">vehicle</span>
  <span class="nav abs" style="left:707px">equipment</span>
  <span class="nav abs" style="left:833px">who we are</span>
  <span class="nav abs" style="left:977px;font-weight:700">contact us</span>
  <svg class="abs" style="left:1072px;top:49px" width="26" height="26" viewBox="0 0 26 26"><circle cx="13" cy="13" r="12" fill="#fff"/><path d="M11 8l5 5-5 5" stroke="#111" stroke-width="2" fill="none"/></svg>

  <div class="serif abs" style="left:94px;top:254px;font-size:33px;color:#fff">For Easy Finance</div>
  <div class="serif abs" style="left:92px;top:296px;font-size:62px;color:#fff;letter-spacing:1px">SOLUTION</div>
  <p class="abs" style="left:94px;top:382px;color:#fff;font-size:14px;line-height:22px">Lorem Ipsum Dolor Sit Amet, Consectetur Adipiscing Elit.<br>Lacinia Eget Vitae Nisi Laoreet Malesuada Id. Commodo Risus</p>
  <div class="cta abs" style="left:94px;top:444px;color:#fff"><span>Get A Quote</span><svg viewBox="0 0 28 28"><circle cx="14" cy="14" r="14" fill="#fff"/><path d="M12 9l5 5-5 5" stroke="#111" stroke-width="2" fill="none"/></svg></div>
  <div class="dots abs"><span></span><span></span><span class="off"></span><span></span><span></span></div>

  <div class="hero-strip abs" role="img" aria-label="Mother and child on a sofa" style="left:719px;top:175px;width:89px;height:353px;background:linear-gradient(180deg,#e7e2dc,#a99e94)"></div>
  <div class="hero-strip abs" role="img" aria-label="Family relaxing at home" style="left:819px;top:246px;width:88px;height:282px;background:linear-gradient(180deg,#f0ede9,#bdb3a9)"></div>
  <div class="hero-strip abs" role="img" aria-label="Child playing on the floor" style="left:918px;top:186px;width:90px;height:320px;background:linear-gradient(180deg,#e4e2df,#9f9890)"></div>
  <div class="hero-strip abs" role="img" aria-label="Child drawing beside a plant" style="left:1017px;top:219px;width:89px;height:323px;background:linear-gradient(180deg,#c9ccc4,#d9d2c8)"></div>
</section>

<section aria-label="About Us">
  <div class="wave-bg abs" role="img" aria-label="Soft flowing wave lines" style="left:0;top:680px;width:1200px;height:750px"></div>
  <div class="photo-city abs" role="img" aria-label="City skyline with glass towers" style="left:92px;top:625px;width:465px;height:683px"></div>
  <h2 class="serif abs" style="left:658px;top:812px;font-size:36px">About Us</h2>
  <h3 class="serif abs" style="left:658px;top:868px;font-size:29px">Makers Of Possible</h3>
  <p class="abs" style="left:658px;top:925px;width:430px">KESTRAL Finance Has Nearly 20 Years Industry Experience, So We Certainly Understand Personal And Business Lending. We Are Committed To Providing Individuals And Businesses With Tailored Financial Services That Enable Them To Reach And Then Exceed Their Financial Goals. &nbsp;We Have A Vast List Of Lenders To Suit Along With An Online Team Ready To Help You, So We're Easily Accessible And Here When You Need Us. Our Friendly Team Of Experienced And Approachable Staff That Will Listen, Understand Your Situation And Lend Responsibly.</p>
  <div class="cta abs" style="left:658px;top:1160px"><span>Learn More</span><svg viewBox="0 0 28 28"><circle cx="14" cy="14" r="14" fill="#111"/><path d="M12 9l5 5-5 5" stroke="#fff" stroke-width="2" fill="none"/></svg></div>
</section>

<section aria-label="Why Choose Us">
  <h2 class="serif abs" style="left:116px;top:1567px;font-size:37px">WHY CHOOSE US?</h2>
  <p class="abs" style="left:116px;top:1632px;width:370px">Well, Because We're Here To Help You! We Care About Outcomes AND Helping You Achieve A Stress And Enjoyable Lending Experience</p>
  <div class="cta abs" style="left:116px;top:1720px"><span>Learn More</span><svg viewBox="0 0 28 28"><circle cx="14" cy="14" r="14" fill="#111"/><path d="M12 9l5 5-5 5" stroke="#fff" stroke-width="2" fill="none"/></svg></div>
  <div class="abs" role="img" aria-label="Businessman with tablet at trading screens" style="left:645px;top:1447px;width:221px;height:427px;background:linear-gradient(180deg,#6a7886,#2f3640 60%,#c9ccd0)"></div>
  <div class="abs" role="img" aria-label="Person signing papers beside a laptop" style="left:876px;top:1447px;width:221px;height:427px;background:linear-gradient(180deg,#7b8088,#d8d9db 55%,#3a3f46)"></div>
</section>

<section aria-label="Vehicle Loan">
  <div class="photo-car abs" role="img" aria-label="Blue sports coupe parked outdoors" style="left:0;top:1971px;width:517px;height:548px"></div>
  <div class="vehicle-panel abs">
    <h2 class="serif abs" style="left:92px;top:104px;font-size:37px">Vehicle Loan</h2>
    <p class="abs" style="left:92px;top:174px;width:440px">While You Focus On Getting The Right Car, We Will Focus On Getting You The Right Finance</p>
    <p class="abs" style="left:92px;top:238px;width:440px">Whether You're Interested In Purchasing A Used Or New Car For Yourself Or A Fleet Of Vehicles Through Your Business, KESTRAL's Team Are Well Equipped To Help You Find The Car Finance That's Right For You.</p>
    <div class="cta abs" style="left:92px;top:342px"><span>Apply Now</span><svg viewBox="0 0 28 28"><circle cx="14" cy="14" r="14" fill="#fff"/><path d="M12 9l5 5-5 5" stroke="#111" stroke-width="2" fill="none"/></svg></div>
  </div>
</section>

<section aria-label="Equipment">
  <div class="wave-bg abs" role="img" aria-label="Soft flowing wave lines" style="left:0;top:2519px;width:1200px;height:582px"></div>
  <h2 class="serif abs" style="left:92px;top:2650px;font-size:37px">Equipment</h2>
  <p class="abs" style="left:92px;top:2747px;width:470px">At KESTRAL, We Help Businesses Of All Sizes To Secure Funding In The Form Of A Business Loan For Asset Purchases From Either A Bank Or Private Lender.</p>
  <p class="abs" style="left:92px;top:2828px;width:470px">Our Dedicated Equipment Finance Specialists Have Extensive Industry Experience Across The Agricultural, Construction And Earthmoving Sectors. We'll Work With You To Understand The Specific Needs That Face Your Business To Keep Your Equipment Up To Date.</p>
  <div class="cta abs" style="left:92px;top:2941px"><span>Apply Now</span><svg viewBox="0 0 28 28"><circle cx="14" cy="14" r="14" fill="#111"/><path d="M12 9l5 5-5 5" stroke="#fff" stroke-width="2" fill="none"/></svg></div>

  <div class="calc abs">
    <h3 class="abs" style="left:30px;top:38px;font-size:24px;font-weight:600">Finance Repayment Calculator</h3>
    <p class="abs" style="left:30px;top:102px;width:400px;font-size:12.5px;line-height:19px">Lorem Ipsum Dolor Sit Amet, Consectetur Adipiscing Elit. Pellentesque Malesuada Adipiscing Sapien Elit, Tempor.</p>
    <label style="top:177px">Purchase Ammount</label><div class="field" style="top:171px">$</div>
    <label style="top:219px">Deposti</label><div class="field" style="top:213px">$</div>
    <label style="top:260px">Tream</label><div class="field" style="top:254px">3 Years</div>
    <label style="top:302px">Intrest Rate %</label><div class="field" style="top:296px">7.5</div>
    <label style="top:344px">Baloon Payment</label><div class="field" style="top:338px">$</div>
    <div class="btn">Calculate</div>
  </div>
</section>

<div class="who-bg abs"></div>
<div class="abs" style="left:0;top:3101px;width:517px;height:67px;background:var(--white)"></div>

<section aria-label="Who We Are">
  <div class="abs" role="img" aria-label="Smiling businesswoman in an office" style="left:80px;top:3171px;width:370px;height:206px;background:linear-gradient(120deg,#d8cfc6,#8d8a86 60%,#c5c7c9)"></div>
  <div class="abs" role="img" aria-label="Colleagues reviewing charts at a table" style="left:80px;top:3390px;width:370px;height:188px;background:linear-gradient(120deg,#3d4043,#7a7c80 55%,#4b4d50)"></div>
  <h2 class="serif abs" style="left:580px;top:3253px;font-size:37px">Who We Are</h2>
  <p class="abs" style="left:580px;top:3318px;width:490px">The Goal Of KESTRAL Finance Is To Build On The Track Record Of The KESTRAL Business And To Create A New Benchmark In The Australia's Asset Finance Industry, Providing Good Old Fashioned Localised Service That Delivers The Assets You Want When You Need Them And Structured To Recognise Asset Useful Life While Being Sensitive To Cashflow.</p>
  <p class="abs" style="left:580px;top:3459px;width:490px">Providing Second To None Asset Finance Support To Business Owners And Individuals Alike</p>
  <div class="cta abs" style="left:580px;top:3523px"><span>Learn More</span><svg viewBox="0 0 28 28"><circle cx="14" cy="14" r="14" fill="#111"/><path d="M12 9l5 5-5 5" stroke="#fff" stroke-width="2" fill="none"/></svg></div>
</section>

<section aria-label="Contact Us">
  <div class="abs" role="img" aria-label="Soft flowing wave lines" style="left:600px;top:3640px;width:600px;height:260px;background:linear-gradient(170deg,rgba(210,218,228,0) 10%,rgba(210,218,228,.8) 50%,rgba(210,218,228,0) 90%)"></div>
  <div class="form-card abs">
    <div class="input" style="top:83px">Full Name</div>
    <div class="input" style="top:137px">Number</div>
    <div class="input" style="top:197px">Regional Location</div>
    <div class="input" style="top:251px">Mail</div>
    <div class="input" style="top:316px">Subject</div>
    <div class="input" style="top:374px;height:97px">Message</div>
    <div class="input" style="top:500px;width:163px;height:37px;font-size:13px;padding:9px 14px">Submit</div>
  </div>
  <h2 class="serif abs" style="left:663px;top:3805px;font-size:37px">Contact Us</h2>
  <div class="abs" style="left:663px;top:3868px;width:440px;font-size:18.5px;line-height:25px">To Find Out How To Get KESTRAL Finance Working For You Helping With Your Funding Needs</div>
  <div class="contact-line abs" style="left:665px;top:3964px"><svg viewBox="0 0 24 24"><path d="M6.6 10.8a15 15 0 006.6 6.6l2.2-2.2a1 1 0 011-.25 11.4 11.4 0 003.6.57 1 1 0 011 1V20a1 1 0 01-1 1A17 17 0 013 4a1 1 0 011-1h3.5a1 1 0 011 1c0 1.250.2 2.450.57 3.57a1 1 0 01-.25 1z" fill="#111"/></svg><span>065550147</span></div>
  <div class="contact-line abs" style="left:665px;top:4020px"><svg viewBox="0 0 24 24"><rect x="2" y="5" width="20" height="14" fill="#111"/><path d="M2 6l10 7 10-7" stroke="#fff" stroke-width="1.6" fill="none"/></svg><span>kestral.finance@harbourmail.co.nz</span></div>
  <div class="contact-line abs" style="left:665px;top:4080px"><svg viewBox="0 0 24 24" style="margin-top:14px"><path d="M22 2L2 10l8.5 3.5L14 22z" fill="#111"/></svg><span style="line-height:27px">PO Box 2208, Marlow<br>Heights, New Zealand</span></div>
</section>

<footer class="footer abs">
  <div class="abs" style="left:92px;top:84px;font-weight:800;font-size:27px;letter-spacing:1px">KESTRAL Finance</div>
  <div class="small abs" style="left:95px;top:134px;width:250px;font-size:10.5px;line-height:14px">KESTRAL Finance Has Nearly 20 Years Industry Experience, So We Certainly Understand Personal And Business Lending.</div>
  <div class="abs" style="left:99px;top:187px;display:flex;gap:9px">
    <span style="width:15px;height:15px;background:#fff"></span><span style="width:15px;height:15px;background:#fff"></span><span style="width:15px;height:15px;background:#fff"></span><span style="width:15px;height:15px;background:#fff"></span>
  </div>
  <div class="divider" style="left:369px"></div>
  <div class="divider" style="left:625px"></div>
  <div class="divider" style="left:857px"></div>

  <h4 style="left:421px;top:60px">Get In Touch</h4>
  <div class="fcontact" style="left:421px;top:112px"><svg viewBox="0 0 24 24"><path d="M6.6 10.8a15 15 0 006.6 6.6l2.2-2.2a1 1 0 011-.25 11.4 11.4 0 003.6.57 1 1 0 011 1V20a1 1 0 01-1 1A17 17 0 013 4a1 1 0 011-1h3.5a1 1 0 011 1c0 1.250.2 2.450.57 3.57a1 1 0 01-.25 1z" fill="#fff"/></svg><span>065550147</span></div>
  <div class="fcontact" style="left:421px;top:145px"><svg viewBox="0 0 24 24"><rect x="2" y="5" width="20" height="14" fill="#fff"/><path d="M2 6l10 7 10-7" stroke="#111" stroke-width="1.6" fill="none"/></svg><span style="font-size:11px">kestral.finance@harbourmail.co.nz</span></div>
  <div class="fcontact" style="left:421px;top:176px"><svg viewBox="0 0 24 24"><path d="M22 2L2 10l8.5 3.5L14 22z" fill="#fff"/></svg><span>PO Box 2208,<br>Marlow Heights,<br>New Zealand</span></div>

  <h4 style="left:678px;top:60px">Useful Links</h4>
  <ul class="flist" style="left:680px;top:104px"><li>Home</li><li>Vehicle</li><li>Culture</li><li>Careers</li><li>Contact</li></ul>

  <h4 style="left:909px;top:60px">Newsletter</h4>
  <div class="small abs" style="left:909px;top:102px;width:200px">Subscribe our newsletter for get our daily news and updates</div>
  <div class="abs" style="left:909px;top:162px;width:195px;height:28px;background:#fff;display:flex;align-items:center">
    <span style="flex:1;color:#999;font-size:9px;padding-left:10px">Enter Your Email</span>
    <span style="width:38px;height:28px;background:#e6e6e6;display:flex;align-items:center;justify-content:center"><svg width="14" height="14" viewBox="0 0 24 24"><path d="M22 2L2 10l8.5 3.5L14 22z" fill="#111"/></svg></span>
  </div>
  <div class="abs" style="left:92px;top:265px;width:1016px;height:1px;background:#555"></div>
  <div class="abs" style="left:0;top:280px;width:1200px;text-align:center;font-size:11.5px">Copyright 2022 KESTRAL Finance</div>
</footer>

</body>
</html>
```